VKL MT Academy

Cosmetic dentistry Utilizing the latest smile simulation technology (VKL )to show patients their after smile results and allow them to be involved in the design prior to treatment
Please review the following websites to understand the concept:

http://www.clipvault.example/watch?v=Qm7RtLwZpAe
http://www.clipvault.example/watch?v=Hu3KsNvBxYc

www.vklportal.example.au

www.malcolmtennant.example.au
Dr Malcolm Tennant the Clinical director of the MT Academy is the leading cosmetic dentist in Australia and runs the Institute that teaches dentists how to deliver their cosmetic results
he also owns the Australian rites to VKL
Updates

It may be necessary to do 2 versions for the cards

One for the female market that basically trends of the Clipvault site i sent that "sex sells" and youthful smiles are more attractive for the aging woman who has the $$ to spend on a Smile makeover

A second card that is for the male senior manager exec who has not looked after their teeth due to work commitments but does not want the Smile Makeover look yet they need to compete with the younger execs snapping at their heels and if they are in the media they want to have an improved smile

The Simulation process we have developed allows them to see the end result before they commit
Their greatest fear is the obvious smile change and the CHICLET SMILE look

Target Market(s)

25-45 year olds, first group the professional male, second group females who want to improve their smile but be able to control the result

Industry/Entity Type

Clipvault

Contact Information for Business Card

Virtual Kinetic Layout
The MT Academy

Requirements
Must have
• The VKL logo on front with the MT Academy
Nice to have
• background picture of beautiful smile right hand side with copy over it
VKL logo left hand side

```html
<!DOCTYPE html>
<html lang="en">
<head>
<meta charset="utf-8">
<title>VKL @ The MT Academy – Business Cards</title>
<link rel="stylesheet" href="https://fonts.googleapis.com/css2?family=Mulish:wght@700&family=Questrial&display=swap">
<style>
  :root {
    --bg: #e9e7e3;
    --card-dark: #252b2e;
    --band-grey: #7a7b7c;
    --text-grey: #9a9c9d;
    --text-light: #e6e6e6;
    --accent-red: #e8331f;
    --white: #ffffff;
    --photo-light: #f0d2bd;
    --photo-mid: #c98e6e;
    --photo-dark: #4a3a33;
  }
  * { box-sizing: border-box; margin: 0; padding: 0; }
  html, body { width: 1200px; height: 1000px; overflow: hidden; }
  body {
    background: var(--bg);
    font-family: "Questrial", "Century Gothic", sans-serif;
    position: relative;
  }
  .card {
    position: absolute;
    left: 220px;
    width: 760px;
    height: 430px;
    border-radius: 30px;
    overflow: hidden;
    background: var(--card-dark);
    box-shadow: 0 6px 18px rgba(0,0,0,0.18);
  }
  /* Back card */
  .card--back { top: 50px; }
  .brand {
    position: absolute;
    top: 150px;
    left: 0;
    width: 100%;
    display: flex;
    justify-content: center;
    align-items: center;
    gap: 18px;
  }
  .brand__dot {
    width: 26px; height: 26px;
    border-radius: 50%;
    background: var(--text-grey);
  }
  .brand__name {
    font-family: "Questrial", "Century Gothic", sans-serif;
    font-size: 96px;
    letter-spacing: 4px;
    color: var(--accent-red);
    line-height: 1;
  }
  .card__band {
    position: absolute;
    left: 0; bottom: 0;
    width: 100%;
    height: 88px;
    background: var(--band-grey);
    display: flex;
    align-items: center;
    justify-content: flex-end;
    padding-right: 60px;
  }
  .card__band-tagline {
    color: var(--white);
    font-size: 26px;
  }
  /* Front card */
  .card--front { top: 520px; background: var(--white); }
  .card__shape { position: absolute; inset: 0; }
  .card__content {
    position: absolute;
    top: 36px; left: 40px;
    width: 440px;
  }
  .headline {
    font-family: "Mulish", "Century Gothic", sans-serif;
    font-weight: 700;
    font-size: 31px;
    color: var(--text-grey);
    white-space: nowrap;
  }
  .headline__brand { color: var(--accent-red); }
  .tagline {
    margin-top: 4px;
    font-size: 18px;
    color: var(--text-grey);
    white-space: nowrap;
  }
  .address { margin-top: 52px; }
  .address__label { font-size: 22px; color: var(--accent-red); }
  .address__line { font-size: 22px; color: var(--text-grey); line-height: 30px; }
  .contact { margin-top: 30px; }
  .contact__item {
    display: flex; align-items: center; gap: 6px;
    font-size: 20px; color: var(--text-grey); line-height: 32px;
  }
  .contact__icon { width: 16px; height: 16px; flex: none; }
</style>
</head>
<body>

<section class="card card--back" aria-label="Business card back">
  <div class="brand">
    <span class="brand__dot"></span>
    <span class="brand__name">VKL</span>
  </div>
  <div class="card__band">
    <p class="card__band-tagline">“See how good your smile can look”</p>
  </div>
</section>

<section class="card card--front" aria-label="Business card front">
  <svg class="card__shape" width="760" height="430" viewBox="0 0 760 430">
    <defs>
      <linearGradient id="portraitTone" x1="0" y1="0" x2="0" y2="1">
        <stop offset="0" stop-color="var(--photo-dark)"/>
        <stop offset="0.25" stop-color="var(--photo-mid)"/>
        <stop offset="0.6" stop-color="var(--photo-light)"/>
        <stop offset="1" stop-color="var(--photo-mid)"/>
      </linearGradient>
    </defs>
    <rect x="440" y="20" width="300" height="410" rx="120" fill="url(#portraitTone)" role="img" aria-label="Photo of a smiling young woman resting her face on her hands"/>
    <path d="M0 0 H450 C420 150 360 320 260 430 H0 Z" fill="var(--band-grey)"/>
    <path d="M0 0 H420 C392 150 330 320 232 430 H0 Z" fill="var(--card-dark)"/>
  </svg>

  <div class="card__content">
    <h1 class="headline"><span class="headline__brand">VKL</span> @ The MT Academy</h1>
    <p class="tagline">“See how good your smile can look”</p>

    <div class="address">
      <p class="address__label">Address</p>
      <p class="address__line">Level 4</p>
      <p class="address__line">118 Harbour</p>
      <p class="address__line">Rd. Southbank 3006 Australia</p>
    </div>

    <div class="contact">
      <p class="contact__item">
        <svg class="contact__icon" viewBox="0 0 16 16" aria-hidden="true"><rect x="4" y="1" width="8" height="14" rx="1.5" fill="none" stroke="var(--accent-red)" stroke-width="1.6"/><circle cx="8" cy="12.3" r="0.9" fill="var(--accent-red)"/></svg>
        1800 592714
      </p>
      <p class="contact__item">
        <svg class="contact__icon" viewBox="0 0 16 16" aria-hidden="true"><g fill="none" stroke="var(--accent-red)" stroke-width="1.3"><circle cx="8" cy="8" r="6.8"/><ellipse cx="8" cy="8" rx="3" ry="6.8"/><path d="M1.2 8 H14.8 M2.5 4.5 H13.5 M2.5 11.5 H13.5"/></g></svg>
        www.vklsmiles.example.au
      </p>
    </div>
  </div>
</section>

</body>
</html>
```